Business cards and letterhead
Business cards and letterhead - Pharmacy/Pharmaceuticals
Creative Brief
Professional
Owen Lilcroft
Partner
4178 Heron Lake Road Suite 410 Grapevine, TX 76099
owen@torvalepz.com
torvalepz.com

```html
<!DOCTYPE html>
<html lang="en">
<head>
<meta charset="utf-8">
<title>Torvale – Business Cards</title>
<link href="https://fonts.googleapis.com/css2?family=Exo+2:wght@400;500;700&display=swap" rel="stylesheet">
<style>
  :root {
    --bg: #e9ecef;
    --card: #ffffff;
    --blue: #1f6fc4;
    --blue-deep: #0f4f9e;
    --blue-light: #4aa3ec;
    --ink-blue: #1a5fae;
    --text-dark: #2b3b52;
    --white: #ffffff;
  }
  * { margin: 0; padding: 0; box-sizing: border-box; }
  html, body { width: 1200px; height: 899px; overflow: hidden; }
  body {
    background: var(--bg);
    font-family: "Exo 2", Arial, sans-serif;
    position: relative;
  }
  .card {
    position: absolute;
    background: var(--card);
    box-shadow: 0 10px 28px rgba(20, 40, 70, 0.18);
    overflow: hidden;
  }

  /* Front card */
  .card-front { left: 540px; top: 60px; width: 560px; height: 320px; }
  .front-brand {
    position: absolute; left: 0; right: 0; top: 112px;
    display: flex; align-items: center; justify-content: center; gap: 16px;
  }
  .brand-dot {
    width: 64px; height: 64px; border-radius: 50%;
    background: var(--blue);
  }
  .brand-name {
    font-weight: 700; font-size: 52px; color: var(--ink-blue);
    letter-spacing: 0.5px;
  }

  /* Back card */
  .card-back { left: 100px; top: 420px; width: 740px; height: 420px; }
  .back-wave { position: absolute; inset: 0; }
  .back-brand {
    position: absolute; left: 34px; top: 32px;
    display: flex; align-items: center; gap: 12px;
  }
  .back-brand .brand-dot { width: 48px; height: 48px; }
  .back-brand .brand-name { font-size: 38px; }

  .contact-list {
    position: absolute; left: 40px; top: 214px;
    list-style: none; color: var(--white); font-size: 15px;
  }
  .contact-list li { display: flex; align-items: center; gap: 12px; height: 27px; }
  .contact-list svg { width: 15px; height: 15px; fill: var(--white); flex: none; }

  .person { position: absolute; left: 468px; top: 146px; }
  .person-name {
    font-size: 26px; font-weight: 400; color: var(--blue);
    letter-spacing: 2px; text-transform: uppercase; line-height: 32px;
  }
  .person-role { font-size: 20px; color: var(--text-dark); line-height: 26px; }

  .address {
    position: absolute; left: 468px; top: 306px;
    color: var(--white); font-size: 15px; line-height: 23px;
  }
  .website {
    position: absolute; left: 344px; top: 376px;
    color: var(--white); font-size: 16px; letter-spacing: 0.5px;
  }
</style>
</head>
<body>

<section class="card card-front" aria-label="Business card front">
  <div class="front-brand">
    <span class="brand-dot"></span>
    <span class="brand-name">Torvale</span>
  </div>
</section>

<section class="card card-back" aria-label="Business card back">
  <svg class="back-wave" viewBox="0 0 740 420" preserveAspectRatio="none">
    <defs>
      <radialGradient id="bandGradient" cx="0.35" cy="0.75" r="0.8">
        <stop offset="0" stop-color="#4aa3ec"/>
        <stop offset="0.55" stop-color="#1f6fc4"/>
        <stop offset="1" stop-color="#0f4f9e"/>
      </radialGradient>
    </defs>
    <path d="M0,150 C200,140 380,230 540,268 C620,286 690,292 740,292 L740,420 L0,420 Z" fill="url(#bandGradient)"/>
    <path d="M0,136 C200,126 380,216 540,254 C620,272 690,278 740,278" fill="none" stroke="#1f6fc4" stroke-width="3"/>
    <path d="M0,192 C200,182 330,244 470,272" fill="none" stroke="#7cc0f4" stroke-width="1.5" opacity="0.6"/>
  </svg>

  <div class="back-brand">
    <span class="brand-dot"></span>
    <span class="brand-name">Torvale</span>
  </div>

  <ul class="contact-list">
    <li>
      <svg viewBox="0 0 24 24"><path d="M6.6 10.8a15.1 15.1 0 0 0 6.6 6.6l2.2-2.2c.3-.3.7-.4 1-.2 1.1.4 2.3.6 3.6.6.6 0 1 .4 1 1V20c0 .6-.4 1-1 1A17 17 0 0 1 3 4c0-.6.4-1 1-1h3.5c.6 0 1 .4 1 1 0 1.3.2 2.5.6 3.6.1.3 0 .7-.2 1z"/></svg>
      <span>010 555 0142</span>
    </li>
    <li>
      <svg viewBox="0 0 24 24"><path d="M7 1h10a2 2 0 0 1 2 2v18a2 2 0 0 1-2 2H7a2 2 0 0 1-2-2V3a2 2 0 0 1 2-2zm0 4v13h10V5zm5 14.5a1 1 0 1 0 0 2 1 1 0 0 0 0-2z"/></svg>
      <span>010 555 0143</span>
    </li>
    <li>
      <svg viewBox="0 0 24 24"><path d="M6 2h9l3 3v5H6zm-2 9h16a2 2 0 0 1 2 2v7H2v-7a2 2 0 0 1 2-2zm3 3v2h4v-2z"/></svg>
      <span>012 555 0187</span>
    </li>
    <li>
      <svg viewBox="0 0 24 24"><path d="M2 5h20v14H2zm2 2v.5l8 5.5 8-5.5V7zm0 3v7h16v-7l-8 5.5z"/></svg>
      <span>owen@torvalepz.com</span>
    </li>
  </ul>

  <div class="person">
    <p class="person-name">Owen Lilcroft</p>
    <p class="person-role">Partner</p>
  </div>

  <p class="address">4178 Heron Lake Road<br>Suite 410 Grapevine</p>

  <p class="website">www.torvalepz.com</p>
</section>

</body>
</html>
```